Would like a website to blog, vlog and post pictures about a upcoming glowtrek road trip in a 1977 kd van.
We will have custom bumper stickers available (by donation or a set amount - unsure) and would like to be able mail these out in the future.
Would like the website to be easy to use, simple. clean with a modern hippie/boho feel.
The travelling van is original green. We have a custom lic plate 'glowtrek'
The stickers are black, white and red.
Our mission:
A Love movement journey to raise the vibration and awareness of Universal Love.
We plan to have it painted with washable paint at certain spots along the way. We will ask willing people to make a journal entry of how they glowtrek (spread the love) and I will quote them in my blog or blog.
The picture attached is me, Dorianne after we painted "Breezy" (the van's given name) with friends for a Canada Day celebration.
The road trip is with my boyfriend and our two 13yr olds - a boy and a girl.
However, the road trip in August is just the beginning of what I envision to be a much longer journey...so I would like the website created to hold space for future adventures :)
Happy creating to whomever feels their heart strings pulled to be part of our glowtrek journey!
With Love and Gratitude,
Dorianne (Band of Glow:)
Please note:
KD pic is for inspiration only - please do not use it on the site. Thank you.

Industry/Entity Type

Paint

Requirements
Must have
• Opt in for Future Newsletter, blog, vlog, join the movement - permission to get creative ;)
Email: dorianne@glowtrek.example

```html
<!DOCTYPE html>
<html lang="en">
<head>
<meta charset="utf-8">
<title>Glowtrek — A Love Movement Journey</title>
<link rel="stylesheet" href="https://fonts.googleapis.com/css2?family=Roboto:ital,wght@0,400;0,500;0,700;1,400&family=Roboto+Condensed:wght@400;700&display=swap">
<style>
:root{
  --red:#e05252;
  --red-dark:#c73a3a;
  --black:#000;
  --band:#3d3d3d;
  --light:#e2e2e2;
  --video-bg:#1c1c1c;
  --footer-bg:#151515;
  --base-bg:#0d0d0d;
  --text:#444;
  --muted:#9a9a9a;
  --white:#fff;
}
*{margin:0;padding:0;box-sizing:border-box}
html,body{width:1200px;height:2308px;overflow:hidden}
body{position:relative;background:var(--white);font-family:"Roboto",Arial,sans-serif;color:var(--text)}
.abs{position:absolute}

/* header */
.site-header{left:0;top:0;width:1200px;height:65px;background:var(--black)}
.brand{left:172px;top:12px;color:var(--white);font-family:"Roboto Condensed",sans-serif;font-weight:700;line-height:1}
.brand-name{font-size:27px;letter-spacing:1px;display:flex;align-items:center;gap:6px}
.brand-dot{width:12px;height:12px;border-radius:50%;background:var(--red)}
.brand-sub{font-size:9px;letter-spacing:1px;margin-top:3px;padding-left:40px}
.main-nav{right:175px;top:0;height:65px;display:flex;align-items:center;gap:36px}
.main-nav a{color:var(--white);text-decoration:none;font-size:11px;text-transform:uppercase}

/* hero */
.hero{left:0;top:65px;width:1200px;height:473px;background:linear-gradient(180deg,#4a4538 0%,#6d5a3e 35%,#3a2a1a 65%,#1f1a12 100%)}
.hero-shade{left:0;top:65px;width:1200px;height:473px;background:radial-gradient(ellipse at 30% 70%,rgba(150,30,20,.45),transparent 55%)}
.hero-title{left:0;top:326px;width:1200px;text-align:center;color:var(--white);font-weight:700;font-size:27px;text-transform:uppercase;letter-spacing:.3px}
.hero-sub{left:0;top:371px;width:1200px;text-align:center;color:var(--white);font-size:23px;text-transform:uppercase}
.hero-arrow{top:262px}

/* donate band */
.donate-band{left:0;top:538px;width:1200px;height:80px;background:var(--band)}
.donate-text{left:174px;top:569px;color:var(--white);font-size:15px}
.btn-donate{left:901px;top:557px;width:127px;height:40px;background:var(--red);color:var(--white);font-weight:500;font-size:14px;display:flex;align-items:center;justify-content:center;border-radius:2px;box-shadow:0 3px 0 var(--red-dark)}

/* headings */
.section-title{color:var(--red);font-weight:500;font-size:16px;text-transform:uppercase}
.pager{display:flex;gap:2px}
.pager span{width:23px;height:22px;background:#d2d2d2;display:flex;align-items:center;justify-content:center}
.pager.dark span{background:#2b2b2b}

/* welcome */
.welcome-photo{left:171px;top:674px;width:323px;height:220px;background:linear-gradient(160deg,#8aa07a,#4b5a3c 55%,#2d2f22)}
.welcome-title{left:538px;top:674px;color:var(--red);font-size:29px;font-weight:500;text-transform:uppercase}
.welcome-copy{left:539px;top:720px;width:470px;font-size:10.5px;line-height:21px;color:#555}
.welcome-copy p+p{margin-top:20px}

/* cards */
.post-card{width:188px}
.post-img{width:188px;height:174px}
.post-title{margin-top:13px;color:var(--red);font-size:12.5px}
.post-date{margin-top:6px;font-style:italic;font-size:10px;color:#555}
.post-rule{margin-top:11px;border-top:1px solid #ccc}
.post-text{margin-top:9px;font-size:10px;line-height:20px;color:#555}

/* gallery */
.gallery-band{left:0;top:1309px;width:1200px;height:301px;background:var(--light)}
.gallery-img{top:1391px;width:188px;height:174px}

/* video */
.video-band{left:0;top:1610px;width:1200px;height:434px;background:var(--video-bg)}
.video-main{left:171px;top:1692px;width:444px;height:309px;background:linear-gradient(180deg,#8cc6ef 0%,#bfe0f5 45%,#b98aa0 75%,#6f5a40 100%)}
.video-bar{left:171px;top:1975px;width:444px;height:26px;background:rgba(20,20,20,.75);display:flex;align-items:center;gap:8px;padding:0 6px}
.video-play{width:26px;height:18px;background:#111;display:flex;align-items:center;justify-content:center}
.video-track{flex:1;height:6px;background:#555}
.video-mark{color:var(--white);font-size:10px;font-weight:700}
.video-item-img{left:643px;width:128px;height:77px}
.video-item-title{left:792px;color:var(--red);font-family:"Roboto Condensed",sans-serif;font-size:12.5px;text-transform:uppercase}
.video-item-text{left:796px;width:240px;font-style:italic;font-size:10px;line-height:20px;color:#8a8a8a}
.video-item-date{left:796px;font-style:italic;font-size:10px;color:var(--white)}
.video-rule{left:643px;width:385px;border-top:1px solid #2e2e2e}

/* footer */
.site-footer{left:0;top:2044px;width:1200px;height:214px;background:var(--footer-bg)}
.footer-brand{left:184px;top:2072px;color:#bdbdbd;font-family:"Roboto Condensed",sans-serif;font-weight:700;line-height:1}
.footer-brand .brand-name{font-size:32px}
.footer-brand .brand-dot{background:#bdbdbd}
.footer-brand .brand-sub{font-size:9px;padding-left:36px}
.footer-links{left:379px;top:2073px;list-style:none;font-size:11px;line-height:21.7px;color:#d0d0d0}
.newsletter{left:491px;top:2071px;width:180px;color:#d0d0d0}
.newsletter h4{font-weight:500;font-size:12.5px;text-transform:uppercase}
.newsletter p{font-size:10.5px;line-height:21px;margin-top:6px}
.nl-input{margin-top:17px;width:178px;height:26px;border:1px solid #3a3a3a;background:#111;color:#bbb;font-size:10px;padding:0 10px;display:flex;align-items:center}
.nl-btn{margin-top:12px;width:178px;height:28px;background:var(--red-dark);color:var(--white);font-size:11px;font-weight:500;display:flex;align-items:center;justify-content:center;text-transform:uppercase}
.address{left:721px;top:2074px;color:#d0d0d0;font-size:10.5px;line-height:21.5px}
.address h5{font-size:10px;font-weight:700;text-transform:uppercase}
.address .row{display:flex;align-items:center;gap:8px}
.social{left:931px;top:2073px;list-style:none;font-size:10px;color:#d0d0d0}
.social li{display:flex;align-items:center;gap:5px;height:21px;margin-bottom:9.5px}
.social .dot{width:21px;height:21px;border-radius:50%;background:#3a3a3a}
.base{left:0;top:2258px;width:1200px;height:50px;background:var(--base-bg);color:#9a9a9a;font-size:10px;display:flex;align-items:center;justify-content:center}
</style>
</head>
<body>

<header class="site-header abs"></header>
<div class="brand abs">
  <div class="brand-name">GLOWTREK<span class="brand-dot"></span></div>
  <div class="brand-sub">GLOWTREK.EXAMPLE</div>
</div>
<nav class="main-nav abs">
  <a>Home</a><a>About Us</a><a>Blog</a><a>Videos</a><a>Gallery</a><a>Donate</a><a>Contact Us</a>
</nav>

<section class="hero abs" role="img" aria-label="Red poppies in a field at sunset under a cloudy sky"></section>
<div class="hero-shade abs"></div>
<svg class="hero-arrow abs" style="left:86px" width="16" height="62" viewBox="0 0 16 62"><polyline points="14,1 2,31 14,61" fill="none" stroke="#fff" stroke-width="1.5"/></svg>
<svg class="hero-arrow abs" style="left:1092px" width="16" height="62" viewBox="0 0 16 62"><polyline points="2,1 14,31 2,61" fill="none" stroke="#fff" stroke-width="1.5"/></svg>
<h1 class="hero-title abs">Its a a love movement journey which we are planing</h1>
<p class="hero-sub abs">To raise the vibration and awareness of universal love.</p>

<div class="donate-band abs"></div>
<p class="donate-text abs">We will have custom bumper stickers available, so whoever donates on our journey will get the stickers.</p>
<div class="btn-donate abs">DONATES</div>

<div class="welcome-photo abs" role="img" aria-label="Painted green vintage van parked on a tree-lined street"></div>
<h2 class="welcome-title abs">Welcome to Glowtrek</h2>
<div class="welcome-copy abs">
  <p>Lorem Ipsum is simply dummy text of the printing and typesetting industry. Lorem Ipsum has been the industry's standard dummy text ever since the 1500s, when an unknown printer took a galley of type and scrambled it to make a type specimen book. It has survived not only five centuries, but also the leap into electronic typesetting, remaining essentially unchanged.</p>
  <p>It was popularised in the 1960s with the release of Letterset sheets containing Lorem Ipsum passages, and more recently with desktop publishing software like Folio PageSetter including versions of Lorem Ipsum.</p>
</div>

<h3 class="section-title abs" style="left:171px;top:938px">Recent Posts</h3>
<div class="pager abs" style="left:980px;top:936px"><span><svg width="6" height="9"><polyline points="5,1 1,4.5 5,8" fill="none" stroke="#fff"/></svg></span><span><svg width="6" height="9"><polyline points="1,1 5,4.5 1,8" fill="none" stroke="#fff"/></svg></span></div>

<article class="post-card abs" style="left:171px;top:978px">
  <div class="post-img" role="img" aria-label="Person with arms outstretched in a hazy field, red overlay" style="background:linear-gradient(180deg,#e8a3a3,#d77a7a);position:relative">
    <svg style="position:absolute;left:79px;top:72px" width="30" height="30" viewBox="0 0 30 30"><circle cx="15" cy="15" r="14" fill="#fff" opacity=".85"/><g fill="none" stroke="#d77a7a" stroke-width="2"><rect x="8" y="12" width="9" height="5" rx="2.5" transform="rotate(-45 12.5 14.5)"/><rect x="13" y="13" width="9" height="5" rx="2.5" transform="rotate(-45 17.5 15.5)"/></g></svg>
  </div>
  <h4 class="post-title" style="font-weight:400">Lorem Ipsum is simply dummy</h4>
  <p class="post-date">Posted on 27 March 2014</p>
  <div class="post-rule"></div>
  <p class="post-text">Lorem Ipsum is simply dummy text of the printing and typesetting...</p>
</article>
<article class="post-card abs" style="left:394px;top:978px">
  <div class="post-img" role="img" aria-label="Family playing together in the water" style="background:linear-gradient(180deg,#3d8fd4,#7cb6e2 50%,#c9a079)"></div>
  <h4 class="post-title" style="font-weight:400">Lorem Ipsum is simply dummy</h4>
  <p class="post-date">Posted on 27 March 2014</p>
  <div class="post-rule"></div>
  <p class="post-text">Lorem Ipsum is simply dummy text of the printing and typesetting...</p>
</article>
<article class="post-card abs" style="left:617px;top:978px">
  <div class="post-img" role="img" aria-label="Two smiling women, one older and one younger" style="background:linear-gradient(90deg,#e7d8cc,#d8b49a 55%,#2a3f7a)"></div>
  <h4 class="post-title" style="font-weight:400">Lorem Ipsum is simply dummy</h4>
  <p class="post-date">Posted on 27 March 2014</p>
  <div class="post-rule"></div>
  <p class="post-text">Lorem Ipsum is simply dummy text of the printing and typesetting...</p>
</article>
<article class="post-card abs" style="left:840px;top:978px">
  <div class="post-img" role="img" aria-label="Woman meditating on green grass outdoors" style="background:linear-gradient(180deg,#cfe0b0,#9cc26a 60%,#6fa23a)"></div>
  <h4 class="post-title" style="font-weight:400">Lorem Ipsum is simply dummy</h4>
  <p class="post-date">Posted on 27 March 2014</p>
  <div class="post-rule"></div>
  <p class="post-text">Lorem Ipsum is simply dummy text of the printing and typesetting...</p>
</article>

<section class="gallery-band abs"></section>
<h3 class="section-title abs" style="left:171px;top:1346px">Photo Gallery</h3>
<div class="pager abs" style="left:980px;top:1343px"><span><svg width="6" height="9"><polyline points="5,1 1,4.5 5,8" fill="none" stroke="#fff"/></svg></span><span><svg width="6" height="9"><polyline points="1,1 5,4.5 1,8" fill="none" stroke="#fff"/></svg></span></div>
<div class="gallery-img abs" style="left:171px;background:linear-gradient(180deg,#6e8a4a,#3f5a2a 60%,#6a6a5a)" role="img" aria-label="Older couple riding bicycles in a park"></div>
<div class="gallery-img abs" style="left:394px;background:linear-gradient(180deg,#e9a24a,#c9741f 55%,#7a4a1a)" role="img" aria-label="Older couple walking in a golden wheat field"></div>
<div class="gallery-img abs" style="left:617px;background:linear-gradient(180deg,#d8e6a8,#e8c8a8 55%,#c89a80)" role="img" aria-label="Baby and mother lying on grass"></div>
<div class="gallery-img abs" style="left:840px;background:linear-gradient(180deg,#2e6cb8,#8cb8e0 55%,#5a7a3a)" role="img" aria-label="Man with open arms under a blue sky"></div>

<section class="video-band abs"></section>
<h3 class="section-title abs" style="left:171px;top:1646px">Video Posts</h3>
<div class="pager dark abs" style="left:980px;top:1643px"><span><svg width="6" height="9"><polyline points="5,1 1,4.5 5,8" fill="none" stroke="#777"/></svg></span><span><svg width="6" height="9"><polyline points="1,1 5,4.5 1,8" fill="none" stroke="#777"/></svg></span></div>
<div class="video-main abs" role="img" aria-label="Children holding hands and jumping in a circle under a blue sky"></div>
<svg class="abs" style="left:369px;top:1821px" width="48" height="48" viewBox="0 0 48 48"><circle cx="24" cy="24" r="23" fill="#fff" opacity=".35"/><polygon points="19,14 35,24 19,34" fill="#fff" opacity=".8"/></svg>
<div class="video-bar abs">
  <div class="video-play"><svg width="8" height="9"><polygon points="0,0 8,4.5 0,9" fill="#fff"/></svg></div>
  <div class="video-track"></div>
  <span class="video-mark">vidmo</span>
</div>

<div class="video-item-img abs" style="top:1693px;background:linear-gradient(180deg,#9cd0f0,#c8a8b8 70%,#7a9a5a)" role="img" aria-label="Children dancing in a circle"></div>
<h4 class="video-item-title abs" style="top:1693px">Lorem Ipsum is simply dummy text</h4>
<p class="video-item-text abs" style="top:1712px">Many desktop publishing packages and web page editors now use...</p>
<p class="video-item-date abs" style="top:1756px">on 27 March 2014</p>
<div class="video-rule abs" style="top:1787px"></div>

<div class="video-item-img abs" style="top:1804px;background:linear-gradient(180deg,#a8c8c0,#5a8a5a 60%,#3a5a3a)" role="img" aria-label="Couple sitting on a hilltop with a backpack"></div>
<h4 class="video-item-title abs" style="top:1804px">Lorem Ipsum is simply dummy text</h4>
<p class="video-item-text abs" style="top:1823px">Many desktop publishing packages and web page editors now use...</p>
<p class="video-item-date abs" style="top:1867px">on 27 March 2014</p>
<div class="video-rule abs" style="top:1900px"></div>

<div class="video-item-img abs" style="top:1919px;background:linear-gradient(180deg,#f0d070,#e8a030 55%,#6a4a20)" role="img" aria-label="Person swinging against a golden sunset"></div>
<h4 class="video-item-title abs" style="top:1919px">Lorem Ipsum is simply dummy text</h4>
<p class="video-item-text abs" style="top:1938px">Many desktop publishing packages and web page editors now use...</p>
<p class="video-item-date abs" style="top:1982px">on 27 March 2014</p>

<footer class="site-footer abs"></footer>
<div class="footer-brand abs" style="top:2110px">
  <div class="brand-name">GLOWTREK<span class="brand-dot"></span></div>
  <div class="brand-sub">GLOWTREK.EXAMPLE</div>
</div>
<ul class="footer-links abs">
  <li>Home</li><li>About Us</li><li>Blog</li><li>Videos</li><li>Gallery</li><li>Testimonials</li><li>Donate</li><li>Contact us</li>
</ul>
<div class="newsletter abs">
  <h4>Newsletter Signup</h4>
  <p>Get our recent updates through your email id</p>
  <div class="nl-input">Enter your email id</div>
  <div class="nl-btn">Subscribe Now</div>
</div>
<div class="address abs">
  <h5>Glowtrek</h5>
  <p>210 Street name,</p>
  <p>State name,&nbsp; Country name,</p>
  <p>Zip code-00000</p>
  <p class="row" style="margin-top:6px"><svg width="11" height="11" viewBox="0 0 24 24"><path fill="#d0d0d0" d="M6.6 10.8a15 15 0 0 0 6.6 6.6l2.2-2.2a1 1 0 0 1 1-.25 11.4 11.4 0 0 0 3.6.57 1 1 0 0 1 1 1V20a1 1 0 0 1-1 1A17 17 0 0 1 3 4a1 1 0 0 1 1-1h3.5a1 1 0 0 1 1 1c0 1.25.2 2.45.57 3.57a1 1 0 0 1-.25 1z"/></svg>(555) 010 0142</p>
  <p class="row"><svg width="11" height="9" viewBox="0 0 22 16"><rect x="1" y="1" width="20" height="14" fill="none" stroke="#d0d0d0" stroke-width="2"/><polyline points="1,1 11,9 21,1" fill="none" stroke="#d0d0d0" stroke-width="2"/></svg>Glowtrek@info</p>
</div>
<ul class="social abs">
  <li><span class="dot"></span>: Circlebook</li>
  <li><span class="dot"></span>: Linkwell</li>
  <li><span class="dot"></span>: Orbit Plus</li>
  <li><span class="dot"></span>: Viewtube</li>
</ul>
<div class="base abs">Copyrights&nbsp; @2014. Glowtrek. All Rights Reserved</div>

</body>
</html>
```